Complete Web project
Start believing in your future
Project: Complete Web project
Complete Web project - Financial Services
Creative Brief
Financial Services
www.pellorinlending.ca
We are a mortgage corporation and finance. We deal only with Business to Business. Our company has been live for 4 years and its the 5th largest in Canada, we do $2.5Billion a year in mortgage financing and growing. We are always looking for better mortgage professionals and seek always to recruit more agents and brokers to our organization. Thus, the website is B2B driven and geared towards recruitment.
I like the website to be unique, cutting edge, clean and professional. Detail within the images is very important to me, such as shadowing and details within the images. Such as, boxing, punched, noise, transparency effects etc. It needs to be highly professional and high-end. Thus, the way you style it needs to be unique and cater to our business. All buttons and navigations should be unique and customized. Its not just the website as a whole which we are paying attention to but the details which are even more important! Dislike: It cannot look like a simple artwork site as if we bought a template theme. IF ITS CHEAP, I WILL JUST DELETE IT.
left side
www.brevantholdings.com
The website should be in a 960px width but the background has to match the inner website so if we zoom out, the site can look and feel in higher width pixelation. Hence, www.brevantholdigns.com. The background flows with the inner site, thus giving it the capability to be in different dimensional widths. On the side panel of homepage, i like to have a "Find an Agent" search bar, you can see an example here: http://www.lendquarry.com/site/on/default.asp (DO NOT REPLACE IT EXACTLY LIKE THEIRS) Transition of colours are also vital, example from Blue to grey or White to grey. Glow effect within header and footer. Example, www.brevantholdings.com. You can see the header and footer there is a glow effect in its background colour.

```html
<!DOCTYPE html>
<html lang="en">
<head>
<meta charset="utf-8">
<title>Pellorin Lending</title>
<link rel="stylesheet" href="https://fonts.googleapis.com/css2?family=Arimo:wght@400;700&family=Tinos:wght@400;700&display=swap">
<style>
:root{
  --blue:#1f77bf;
  --blue-dark:#0d4f8c;
  --blue-deep:#0a3f73;
  --blue-light:#5fb4ee;
  --green:#8cbf3f;
  --green-dark:#6a9a22;
  --ink:#333;
  --muted:#666;
  --grey-bg:#e9ecef;
  --grey-line:#cfd4d9;
  --white:#fff;
}
*{box-sizing:border-box;margin:0;padding:0}
html,body{width:1200px;height:978px;overflow:hidden}
body{font-family:"Arimo",Arial,sans-serif;color:var(--ink);background:var(--white);position:relative;font-size:11px}
.abs{position:absolute}

/* header */
.utility{left:745px;top:0;display:flex;gap:12px}
.utility a{display:block;height:22px;line-height:22px;padding:0 12px;font-size:10px;color:var(--white);text-decoration:none;border-radius:0 0 3px 3px;white-space:nowrap}
.utility .find{background:linear-gradient(#9fcb55,var(--green-dark));width:148px;text-align:center}
.utility .login{background:linear-gradient(#555,#222);width:106px;text-align:center}
.brand{left:185px;top:30px;display:flex;align-items:center;gap:10px}
.brand-mark{width:20px;height:20px;background:var(--blue)}
.brand-name{font-family:"Tinos",serif;font-size:23px;color:var(--blue-dark);font-weight:400;white-space:nowrap}
.nav{left:383px;top:61px;display:flex;gap:9px}
.nav a{height:42px;line-height:42px;padding:0;font-size:13px;color:var(--white);text-decoration:none;border-radius:3px;background:linear-gradient(#4aa6e6,var(--blue));box-shadow:0 2px 3px rgba(0,0,0,.25);text-align:center;white-space:nowrap}
.nav a.active{background:linear-gradient(#a6d35c,var(--green-dark));color:#234}
.nav .w1{width:72px}.nav .w2{width:80px}.nav .w3{width:140px}.nav .w4{width:82px}.nav .w5{width:127px}.nav .w6{width:82px}

/* hero band */
.band{left:0;top:119px;width:1200px;height:357px;background:radial-gradient(ellipse at 50% 45%,#5db8f2 0%,#1d83cf 55%,#0c5ea7 100%)}
.slider{left:185px;top:132px;width:825px;height:330px;border:4px solid var(--white);box-shadow:0 4px 12px rgba(0,0,0,.35);overflow:hidden}
.slide-img{width:100%;height:100%;background:linear-gradient(180deg,#b9d2e6 0%,#9aa79a 45%,#5e7350 100%)}
.caption{left:0;bottom:0;width:100%;height:40px;line-height:40px;background:rgba(0,0,0,.7);color:var(--white);font-size:16px;padding-left:14px;white-space:nowrap}
.arrow{top:282px}
.arrow.prev{left:164px}.arrow.next{left:1018px}

/* content */
.welcome{left:185px;top:500px;width:560px}
.heading{font-family:"Tinos",serif;color:var(--blue);font-size:18px;font-weight:400}
.welcome p{margin-top:6px;font-size:11px;line-height:14px;color:var(--muted)}
.read-more{display:inline-block;margin-top:7px;font-family:"Tinos",serif;font-size:14px;color:var(--blue-dark);font-weight:700}
.testimonial{left:185px;top:621px;width:259px;height:172px;border:1px solid var(--grey-line);background:var(--white);box-shadow:0 2px 5px rgba(0,0,0,.15);padding:10px}
.testimonial h3{font-family:"Tinos",serif;font-weight:400;font-size:15px;color:var(--blue)}
.t-photo{position:absolute;left:10px;top:34px;width:78px;height:100px;border:3px solid var(--white);box-shadow:0 1px 4px rgba(0,0,0,.3);background:linear-gradient(#c8cfd6,#e6d6c5)}
.t-text{position:absolute;left:100px;top:36px;width:148px;font-size:9px;line-height:12px;color:var(--muted)}
.t-name{position:absolute;left:10px;top:146px;font-size:11px;color:var(--blue)}
.t-dots{position:absolute;right:12px;top:150px;display:flex;gap:3px}
.t-dots i{width:6px;height:6px;border-radius:50%;background:#999}
.video{left:470px;top:621px;width:260px;height:168px;border:1px solid var(--grey-line);box-shadow:0 2px 5px rgba(0,0,0,.15)}
.video-img{width:100%;height:146px;background:linear-gradient(#6a8fb8,#c9cfd4 60%,#6f7f5c)}
.video-bar{height:20px;background:linear-gradient(#3a3a3a,#111);display:flex;align-items:center;padding:0 6px;gap:6px}
.video-bar .track{flex:1;height:4px;background:#555;border-radius:2px}

.search{left:756px;top:507px;width:254px;height:286px;border:1px solid var(--grey-line);background:var(--white);box-shadow:0 2px 6px rgba(0,0,0,.18)}
.search h2{height:35px;line-height:35px;background:linear-gradient(#3a93d6,var(--blue-dark));color:var(--white);font-family:"Tinos",serif;font-weight:400;font-size:16px;padding-left:12px;white-space:nowrap}
.search form{padding:8px 12px}
.search label{display:block;color:var(--blue);font-size:13px;margin-top:8px}
.search .field{margin-top:4px;height:22px;border:1px solid #bbb;background:var(--white);font-size:10px;color:#888;line-height:20px;padding-left:6px;position:relative}
.search .field.select::after{content:"";position:absolute;right:2px;top:2px;width:16px;height:16px;background:#ddd;border-left:1px solid #bbb}
.search .go{margin-top:14px;width:66px;height:26px;line-height:26px;text-align:center;color:var(--white);font-size:12px;border-radius:3px;background:linear-gradient(#a6d35c,var(--green-dark))}

/* footer */
.footer{left:0;top:820px;width:1200px;height:121px;background:linear-gradient(#f3f4f5,var(--grey-bg));border-top:1px solid var(--grey-line)}
.f-col{top:828px}
.f-col h4{font-family:"Tinos",serif;font-weight:400;font-size:15px;color:var(--blue);margin-bottom:8px;white-space:nowrap}
.f-col li{list-style:none;font-size:10px;line-height:19px;color:var(--ink);white-space:nowrap}
.f-col li::before{content:"";display:inline-block;width:4px;height:4px;background:var(--green);margin-right:7px;vertical-align:middle}
.links{left:190px;width:250px}
.links ul{display:grid;grid-template-columns:1fr 1fr}
.contact{left:460px;width:200px}
.contact p{font-size:10px;line-height:19px}
.contact b{color:var(--blue);font-weight:400;display:inline-block;width:38px}
.newsletter{left:682px;width:200px}
.newsletter p{font-size:10px;line-height:14px;color:var(--muted)}
.nl-form{display:flex;margin-top:12px;gap:6px}
.nl-input{width:130px;height:22px;border:1px solid #bbb;background:var(--white);font-size:9px;color:#999;line-height:20px;padding-left:6px}
.nl-btn{width:50px;height:22px;line-height:22px;text-align:center;color:var(--white);font-size:10px;border-radius:3px;background:linear-gradient(#a6d35c,var(--green-dark))}
.follow{left:904px;width:106px}
.follow .row{display:flex;justify-content:space-between;align-items:center;font-size:10px;height:28px}
.follow .sq{width:16px;height:16px;background:var(--blue-dark)}
.divider{top:828px;width:1px;height:104px;background:var(--grey-line)}
.bottom{left:0;top:941px;width:1200px;height:37px;background:linear-gradient(#124f88,var(--blue-deep));color:var(--white);font-size:10px}
.bottom span{position:absolute;top:12px;white-space:nowrap}
</style>
</head>
<body>

<header>
  <nav class="utility abs">
    <a class="find" href="#">Find an Agent</a>
    <a class="login" href="#">Member Login</a>
  </nav>
  <div class="brand abs"><span class="brand-mark"></span><span class="brand-name">Pellorin Lending</span></div>
  <nav class="nav abs">
    <a class="active w1" href="#">Home</a>
    <a class="w2" href="#">About Us</a>
    <a class="w3" href="#">Products &amp; Services</a>
    <a class="w4" href="#">Apply Now</a>
    <a class="w5" href="#">Tools &amp; Resources</a>
    <a class="w6" href="#">Contact Us</a>
  </nav>
</header>

<section class="band abs"></section>
<div class="slider abs">
  <div class="slide-img" role="img" aria-label="Family standing in front of their new brick house"></div>
  <div class="caption abs">We are a mortgage corporation and finance. We deal only with Business to Business.</div>
</div>
<svg class="arrow prev abs" width="16" height="24" viewBox="0 0 16 24"><path d="M12 2 3 12l9 10" fill="none" stroke="#fff" stroke-width="4"/></svg>
<svg class="arrow next abs" width="16" height="24" viewBox="0 0 16 24"><path d="M4 2l9 10-9 10" fill="none" stroke="#fff" stroke-width="4"/></svg>

<main>
  <section class="welcome abs">
    <h1 class="heading">Welcome to Pellorin Lending</h1>
    <p>Lorem ipsum dolor sit amet, consectetur adipiscing elit, sed do eiusmod tempor incididunt ut labore et dolore magna aliqua. Ut enim ad minim veniam, quis nostrud exercitation ullamco laboris nisi ut aliquip ex ea commodo consequat. Duis aute irure dolor in reprehenderit in voluptate velit esse cillum dolore eu fugiat nulla pariatur. Excepteur sint occaecat cupidatat non proident, sunt in culpa qui officia deserunt mollit anim id est laborum.</p>
    <a class="read-more" href="#">Read More...</a>
  </section>

  <article class="testimonial abs">
    <h3>Testmonial</h3>
    <div class="t-photo" role="img" aria-label="Portrait of a smiling client"></div>
    <p class="t-text">“ Lorem ipsum dolor sit amet, consectetur adipiscing elit sed do eiusmod tempor incididunt ut labore et dolore magna aliqua. Ut enim ad minim veniam quis nostrud exercitation ullamco. ”</p>
    <span class="t-name">Dana Ferrow</span>
    <span class="t-dots"><i></i><i></i><i></i></span>
  </article>

  <div class="video abs">
    <div class="video-img" role="img" aria-label="Video still of a two-storey family home"></div>
    <div class="video-bar">
      <svg width="10" height="10" viewBox="0 0 10 10"><path d="M1 0l8 5-8 5z" fill="#fff"/></svg>
      <div class="track"></div>
      <svg width="12" height="10" viewBox="0 0 12 10"><path d="M0 3h3l4-3v10L3 7H0z" fill="#fff"/></svg>
    </div>
  </div>

  <aside class="search abs">
    <h2>Search Mortgages Agent</h2>
    <form>
      <label>By Name</label><div class="field">Name</div>
      <label>By City</label><div class="field select">Select City</div>
      <label>By Language</label><div class="field select">Select City</div>
      <div class="go">Search</div>
    </form>
  </aside>
</main>

<footer>
  <div class="footer abs"></div>
  <div class="f-col links abs">
    <h4>Quick Links</h4>
    <ul><li>Home</li><li>Apply Now</li><li>About Us</li><li>Tools &amp; Resources</li><li>Products &amp; Services</li><li>Contact</li></ul>
  </div>
  <div class="divider abs" style="left:448px"></div>
  <div class="f-col contact abs">
    <h4>Contact Information</h4>
    <p><b>Email :</b> info@lorem.com</p>
    <p><b>Phone :</b> (000) 000 - 0000</p>
  </div>
  <div class="divider abs" style="left:670px"></div>
  <div class="f-col newsletter abs">
    <h4>Newsletter</h4>
    <p>Lorem Ipsum is simply dummy text of the printing and typesetting industry.</p>
    <div class="nl-form"><div class="nl-input">Enter Your Email</div><div class="nl-btn">Signup</div></div>
  </div>
  <div class="divider abs" style="left:892px"></div>
  <div class="f-col follow abs">
    <h4>Follow Us</h4>
    <div class="row">Friendsheet<span class="sq"></span></div>
    <div class="row">Chirpline<span class="sq"></span></div>
    <div class="row">Linkwork<span class="sq"></span></div>
  </div>
  <div class="bottom abs">
    <span style="left:190px">Terms &amp; Conditions</span>
    <span style="left:846px">Copyright © 2013. All Rights Reserved.</span>
  </div>
</footer>

</body>
</html>
```